web site to find a reliable, local tradesman, handyman or builder for any job

Design a web site as marketplace for handyman and client.
Handyman can
* set their profile (name, address, contacts)
* search / view / apply for job offers (by setting a new offer)
Client can
* search / view job offers
* generate new job offers (title, description, max price, date, duration, location).
* select and rate a job
Main functions would be SEARCH / VIEW to see in one glance WHAT needs to be done WHERE. The contractors then exchange contacts.
Handyman

```html
<!DOCTYPE html>
<html lang="en">
<head>
<meta charset="utf-8">
<title>Handy Hunt – Find a Handyman or a Client</title>
<link rel="stylesheet" href="https://fonts.googleapis.com/css2?family=Sorts+Mill+Goudy&family=Open+Sans:wght@400;600;700&display=swap">
<style>
:root{
  --slate:#5b5b80;
  --slate-dark:#46466a;
  --slate-deep:#3a3a62;
  --navy:#2f2f66;
  --olive:#a9a845;
  --olive-light:#cfcf7a;
  --olive-pale:#d8d68e;
  --field:#f1efd6;
  --white:#ffffff;
  --paper:#e9eaec;
}
*{box-sizing:border-box;margin:0;padding:0}
html,body{width:1200px;height:900px;overflow:hidden}
body{position:relative;background:var(--white);font-family:"Open Sans",sans-serif;color:var(--white)}
.abs{position:absolute}
.serif{font-family:"Sorts Mill Goudy",serif}

/* header */
.site-header{left:0;top:0;width:1200px;height:113px;background:radial-gradient(ellipse at 45% 30%,#6e6e94 0%,var(--slate) 55%,var(--slate-dark) 100%)}
.brand{left:86px;top:36px;display:flex;align-items:center;gap:10px;font-family:"Sorts Mill Goudy",serif;font-size:30px;letter-spacing:2px;color:var(--white)}
.brand-dot{width:24px;height:24px;border-radius:50%;background:var(--slate-deep)}
.tagline{right:30px;top:9px;font-size:20px}
.phone{right:38px;top:32px;font-size:24px;font-weight:700;letter-spacing:1px}
.main-nav{left:400px;top:66px;width:776px;height:32px;border-radius:8px;background:linear-gradient(#d4d48a,var(--olive) 60%,#8d8c30);box-shadow:0 2px 3px rgba(0,0,0,.35);display:flex;justify-content:space-around;align-items:center;padding:0 10px}
.main-nav a{color:var(--navy);text-decoration:none;font-size:19px}

/* hero */
.hero-backdrop{left:88px;top:113px;width:1024px;height:680px;background:linear-gradient(135deg,#f4f4f6 0%,var(--paper) 45%,#d2d4d8 70%,#eeeeef 100%)}
.person-left{left:88px;top:166px;width:212px;height:427px;border-radius:90px 90px 0 0;background:linear-gradient(#8a7c70 0%,#2b2b2b 30%,#3d3a35 70%,#5e6f88 100%)}
.person-right{left:852px;top:166px;width:258px;height:427px;border-radius:110px 110px 0 0;background:linear-gradient(#b99a82 0%,#4a4f6c 35%,#3d4260 100%)}

.job-search{left:545px;top:125px;display:flex;align-items:center;gap:12px}
.job-search .label{font-size:16px;font-weight:600;color:var(--navy);letter-spacing:.5px}
.job-field{height:26px;background:var(--olive);color:var(--navy);font-size:17px;font-weight:600;padding:2px 16px}
.job-btn{left:1008px;top:125px;width:98px;height:26px;border-radius:13px;background:linear-gradient(#cfcf7a,var(--olive));color:var(--navy);font-size:14px;padding:3px 9px;display:flex;align-items:center;gap:4px}

.register{left:386px;top:174px;width:429px;height:195px;background:linear-gradient(160deg,#d6d48b,var(--olive-light) 50%,#b5b44f)}
.register h2{position:absolute;left:41px;top:14px;font-weight:400;font-size:21px;color:var(--navy)}
.radio{position:absolute;top:46px;display:flex;align-items:center;gap:12px;font-size:21px;color:var(--navy)}
.radio i{width:18px;height:18px;border-radius:50%;background:var(--white);display:flex;align-items:center;justify-content:center}
.radio i b{width:8px;height:8px;border-radius:50%;background:var(--navy)}
.reg-label{position:absolute;left:54px;font-size:18px;color:var(--navy);letter-spacing:1px}
.reg-input{position:absolute;left:197px;width:151px;height:21px;background:var(--field)}
.submit{position:absolute;left:220px;top:168px;width:108px;height:22px;border-radius:11px;background:var(--field);color:var(--navy);font-size:18px;text-align:center;line-height:22px;letter-spacing:1px}

.finder{height:112px;border-radius:8px;background:rgba(75,75,115,.92)}
.finder h2{position:absolute;left:10px;top:6px;font-weight:400;font-size:31px;color:var(--white)}
.finder .field{position:absolute;top:58px;height:25px;background:var(--white);color:#111;font-size:12px;padding:5px 3px;font-weight:600}
.finder .go{position:absolute;top:56px;width:46px;height:29px;border-radius:8px;background:var(--olive-light);color:var(--navy);font-size:15px;text-align:center;line-height:29px}
.select-arrow{position:absolute;right:2px;top:4px;width:12px;height:16px;background:var(--slate-deep)}

/* categories */
.categories{left:88px;top:592px;width:1020px;height:145px;background:var(--slate)}
.categories h3{position:absolute;left:18px;top:7px;font-weight:400;font-size:14px}
.cat-col{position:absolute;top:32px;list-style:none;font-size:14px;line-height:17.2px;letter-spacing:.3px}

/* footer */
.site-footer{left:0;top:793px;width:1200px;height:107px;background:radial-gradient(ellipse at 40% 40%,#5c5c82,var(--slate-dark) 70%,#3e3e62)}
.copyright{left:52px;top:47px;font-size:19px}
.social{top:33px;width:48px;height:48px;border-radius:6px}
</style>
</head>
<body>

<header class="site-header abs">
  <div class="brand abs"><span>HANDY HUNT</span><span class="brand-dot"></span></div>
  <p class="tagline abs serif">For all Minor and Major Home Repairs - Call</p>
  <p class="phone abs">0800 555 0199</p>
  <nav class="main-nav abs serif">
    <a href="#">Home</a><a href="#">Find a Handyman</a><a href="#">Find a Client</a><a href="#">Job Offers</a><a href="#">Contact Us</a>
  </nav>
</header>

<div class="hero-backdrop abs" role="img" aria-label="Backdrop of architectural blueprints, perforated metal sheets and a folding ruler"></div>
<div class="person-left abs" role="img" aria-label="Young handyman in a black T-shirt holding a power drill, wearing a tool belt"></div>
<div class="person-right abs" role="img" aria-label="Smiling tradesman in a work shirt with arms crossed"></div>

<form class="job-search abs">
  <span class="label">JOB OFFERS</span>
  <span class="job-field" style="width:208px">What ?</span>
  <span class="job-field" style="width:114px">Where ?</span>
</form>
<div class="job-btn abs">search
  <svg width="28" height="20" viewBox="0 0 28 20"><circle cx="10" cy="8" r="6" fill="#e8e8e8" stroke="#777" stroke-width="2"/><line x1="14" y1="12" x2="24" y2="18" stroke="#555" stroke-width="3" stroke-linecap="round"/></svg>
</div>

<section class="register abs serif">
  <h2>New Users Register yourself FREE</h2>
  <label class="radio" style="left:45px"><i><b></b></i>Handyman</label>
  <label class="radio" style="left:231px"><i></i>Client</label>
  <span class="reg-label" style="top:79px">NAME</span><span class="reg-input" style="top:79px"></span>
  <span class="reg-label" style="top:110px">EMAIL</span><span class="reg-input" style="top:108px"></span>
  <span class="reg-label" style="top:141px">ADDRESS</span><span class="reg-input" style="top:137px"></span>
  <span class="submit">SUBMIT</span>
</section>

<section class="finder abs" style="left:230px;top:396px;width:283px">
  <h2 class="serif">Find a Handyman</h2>
  <span class="field" style="left:10px;width:136px">search by category<span class="select-arrow"></span></span>
  <span class="field" style="left:166px;width:44px">zip</span>
  <span class="go" style="left:233px">Go</span>
</section>

<section class="finder abs" style="left:704px;top:396px;width:285px">
  <h2 class="serif" style="left:8px">Find a Client</h2>
  <span class="field" style="left:9px;width:138px">search</span>
  <span class="field" style="left:170px;width:44px">zip</span>
  <span class="go" style="left:237px">Go</span>
</section>

<section class="categories abs">
  <h3>Categories</h3>
  <ul class="cat-col" style="left:37px"><li>Air Conditioning</li><li>Architect</li><li>Attics and Basements</li><li>Basements</li><li>Bathroom Remodelling</li><li>Cabinets</li></ul>
  <ul class="cat-col" style="left:253px"><li>Carpentry</li><li>Cleaning</li><li>Closets and Storage</li><li>Custom Home Building</li><li>Decks</li><li>Demolitions and Disposal</li></ul>
  <ul class="cat-col" style="left:496px"><li>Dry wall and Plastering</li><li>Electrical</li><li>Excavation</li><li>Fencing</li><li>Foundations/ Retain Walls</li><li>Garages/ Outbuildings</li></ul>
  <ul class="cat-col" style="left:748px"><li>Kitchen Remodeling</li><li>Landscaping</li><li>Painting/ Wallcovering</li><li>Plumbing</li><li>Roofing</li><li>Windows and Doors</li></ul>
</section>

<footer class="site-footer abs">
  <p class="copyright abs serif">2011 Copyrights Reserved</p>
  <a class="social abs" href="#" aria-label="Video channel" style="left:938px;background:#d8d8dc"></a>
  <a class="social abs" href="#" aria-label="Social network page" style="left:1014px;background:#4a68a8"></a>
  <a class="social abs" href="#" aria-label="Microblog feed" style="left:1090px;background:#5cb6e2"></a>
</footer>

</body>
</html>
```